Progressive business consultancy seeking "Accounting Industry Flyer"

We are looking for an industry flyer that we will use with potential clients/prospects that outlines our skills and experience in delivering change across the Accounting Services Industry. The flyer will be used to help potential clients understand the challenges and issues faced by the accounting industry and how our service offerings can help them solve their project challenges and problems.

About Us:
Based in Melbourne, Australia, Vendor-o is a management consulting organisation that partners with their clients to lead the execution of strategic process and system improvement initiatives.

Vendor-o offers business advisory services in Project Management, Business Process Management, Change Management, Business Analysis and Business Intelligence. Vendor-o combines hands on delivery with coaching in best practice methodologies and approaches to build our clients capabilities ensuring their ongoing success in project implementations.

Vendor-o has extensive experience across a wide range of industries. We specialise in assisting organisations across the accounting, legal, financial services and health sectors.

Our core purpose is to help businesses in the middle market navigate transformational change through clear and focused execution and enablement.

www.vendor-o.com.au
@vendor_o

What we're looking for:

A professional, corporate, industry flyer providing an overview of our capabilities and experience in the accounting industry. Focus is on the "e" in vendor-o. The look should be sharp and crisp, with a professional and corporate feel. The target for the flyer is Accountants and Mid-Tier Accounting Firms.

The Vendor-o colours are white and blue (RGB:0/86/162 and
CMYK 97/73/4/0)

A professional, corporate theme that is consistent across both sides of the flyer. The design should reflect our focus on the "e" in vendor-o, which is what we're really about - "e"xecution and "e"nablement of change.

I've attached a PNG file of our word template which shows the focus on the "e" as a watermark on the document as well as the font files if required.

Let me know if you need any further information or design specifics.

Thanks,

Felicity
(on behalf of Gregory)
Updates

Hi All, Thanks for your design submissions so far. We have discovered that our hero image has not been attached to the brief. Please find the jpeg attached now. It has been loaded as "Vendor-o Hero Image.jpg" Thanks Gregory @vendor_o

Reason: Hi Designers, Thanks to everyone who has taken the time to make a submission on our contest. We really appreciate it. We have decided to extend our deadline by 5 days so we can review the designs with other colleagues and provide feedback to everyone who has made a submission. Thanks for all your creative designs. Gregory @vendor_o

Reason: Hi designers, thanks to everyone for taking the time to submit their designs. We are going to have to extend our deadline again as we haven't had an opportunity to review all of the designs properly and provide feedback.

Target Market(s)

Accountants and Accounting Firms (mid tier firms)

Industry/Entity Type

Management Consulting

Font styles to use
Other font styles liked:
• Calibri & Attached font files.

Colors
0455a3
3277b5
ffffff

Requirements
Must have
• A Professional A4 double sided colour flyer consisting of:
• Front Page:
• - hero image (attached)
• - Draft content front (attached)
• - Vendor-o Logo (attached)
• Back Page
• - Draft content back (attached)

```html
<!DOCTYPE html>
<html lang="en">
<head>
<meta charset="utf-8">
<title>Vendor-o – What We Do</title>
<link rel="stylesheet" href="https://fonts.googleapis.com/css2?family=Exo+2:wght@400;600;700;800&display=swap">
<style>
  :root {
    --page-blue: #2f4c9c;
    --circle-blue: #1f72be;
    --white: #ffffff;
    --soft-white: #eef2fb;
  }
  * { margin: 0; padding: 0; box-sizing: border-box; }
  html, body { width: 849px; height: 1200px; overflow: hidden; }
  body {
    background: var(--page-blue);
    font-family: "Exo 2", Arial, sans-serif;
    color: var(--white);
  }
  .flyer { position: relative; width: 849px; height: 1200px; }
  .headline {
    position: absolute; top: 92px; left: 0; width: 100%;
    text-align: center; font-weight: 800; font-size: 104px;
    letter-spacing: 1px; line-height: 1;
  }
  .service {
    position: absolute; width: 210px; margin-left: -105px;
    text-align: center;
  }
  .service-icon {
    display: block; width: 132px; height: 132px; margin: 0 auto;
    border-radius: 50%; background: var(--circle-blue);
  }
  .service-title {
    margin-top: 27px; font-weight: 700; font-size: 18px; line-height: 21px;
    min-height: 42px;
  }
  .service-text {
    margin-top: 26px; font-weight: 400; font-size: 14px; line-height: 18px;
    color: var(--soft-white);
  }
  .row-one { top: 270px; }
  .row-two { top: 608px; }
  .brand {
    position: absolute; top: 1024px; left: 0; width: 100%;
    text-align: center; font-weight: 600; font-size: 66px; line-height: 1;
    letter-spacing: 1px;
  }
  .contact {
    position: absolute; top: 1126px; left: 0; width: 100%;
    text-align: center; font-size: 13px; line-height: 19px;
  }
  .contact strong { font-weight: 700; }
</style>
</head>
<body>
<main class="flyer">
  <h1 class="headline">WHAT WE DO</h1>

  <section class="service row-one" style="left:320px">
    <span class="service-icon" role="img" aria-label="Icon of an organisation chart of people"></span>
    <h2 class="service-title">Project<br>Management</h2>
    <p class="service-text">Delivering High Quality projects on time and within budget.</p>
  </section>

  <section class="service row-one" style="left:528px">
    <span class="service-icon" role="img" aria-label="Icon of a presenter at a board with an audience"></span>
    <h2 class="service-title">Business Process<br>Management</h2>
    <p class="service-text">Engaging your people to understand current practices and develop smarter business processes</p>
  </section>

  <section class="service row-two" style="left:215px">
    <span class="service-icon" role="img" aria-label="Icon of two people exchanging with circular arrows"></span>
    <h2 class="service-title">Change<br>Management</h2>
    <p class="service-text">Building engagement through business understanding, clear communication and relevant capability.</p>
  </section>

  <section class="service row-two" style="left:424px">
    <span class="service-icon" role="img" aria-label="Icon of a person beside a chart board"></span>
    <h2 class="service-title">Business<br>Analysis</h2>
    <p class="service-text">Building inovative links between your department, driving collaboration and providing holistic business solutions.</p>
  </section>

  <section class="service row-two" style="left:633px">
    <span class="service-icon" role="img" aria-label="Icon of a person with gears and a dollar sign"></span>
    <h2 class="service-title">Business<br>Intelligence</h2>
    <p class="service-text">Leveraging one of your organizations most valuable assets – your data.</p>
  </section>

  <div class="brand">Vendor-o</div>

  <p class="contact">Check out our website at <strong>www.vendor-o.com.au</strong> and contact us on <strong>(+61) 3 9555 0123</strong><br>to help your organisation navigate change and drive successful business outcomes.</p>
</main>
</body>
</html>
```